arts & crafts

I collect old plates & make them into serving plates for cakes, afternoon teas, special occasions, weddings, parties, bridal showers. cake competitions, displays in bakeries.

Contact Information for Business Card

Tulips Turn Gold
Bringing the old back to new
Ph 0412873905
info@ tulipsturngold.com.au
www.tulipsturngold.com.au
facebook
Craftly

```html
<!DOCTYPE html>
<html lang="en">
<head>
<meta charset="utf-8">
<title>Tulips Turn Gold – Business Card</title>
<link rel="stylesheet" href="https://fonts.googleapis.com/css2?family=Gabriela&family=Dancing+Script:wght@700&display=swap">
<style>
  :root {
    --page-bg: #e9e9ea;
    --card-bg: #ffffff;
    --brand-blue: #6874b8;
    --tagline-white: #ffffff;
  }
  * { margin: 0; padding: 0; box-sizing: border-box; }
  html, body {
    width: 1200px;
    height: 1016px;
    overflow: hidden;
    background: var(--page-bg);
  }
  .business-card {
    position: absolute;
    left: 50px;
    top: 203px;
    width: 1100px;
    height: 610px;
    background: var(--card-bg);
    overflow: hidden;
    box-shadow: 0 2px 6px rgba(0,0,0,0.12);
  }
  .brand-mark {
    position: absolute;
    left: 128px;
    top: 144px;
    width: 290px;
    height: 290px;
    border: 5px solid var(--brand-blue);
    border-radius: 50%;
    display: flex;
    align-items: center;
    justify-content: center;
  }
  .brand-name {
    font-family: "Gabriela", serif;
    font-size: 36px;
    line-height: 1.25;
    color: var(--brand-blue);
    text-align: center;
  }
  .contact-list {
    position: absolute;
    left: 564px;
    top: 130px;
    list-style: none;
    font-family: "Gabriela", serif;
    color: var(--brand-blue);
  }
  .contact-shop {
    font-size: 30px;
    margin-left: 5px;
    height: 56px;
  }
  .contact-item {
    display: flex;
    align-items: center;
    height: 56px;
  }
  .contact-item svg {
    width: 34px;
    height: 34px;
    margin-right: 9px;
    flex: none;
  }
  .contact-phone { font-size: 29px; }
  .contact-email, .contact-web { font-size: 22px; }
  .contact-social { font-size: 24px; }
  .tagline-band {
    position: absolute;
    left: 0;
    top: 458px;
    width: 1100px;
    height: 152px;
  }
  .tagline {
    position: absolute;
    left: 67px;
    top: 505px;
    font-family: "Dancing Script", cursive;
    font-weight: 700;
    font-size: 36px;
    color: var(--tagline-white);
  }
</style>
</head>
<body>
  <div class="business-card">
    <div class="brand-mark">
      <p class="brand-name">Tulips<br>Turn Gold</p>
    </div>

    <ul class="contact-list">
      <li class="contact-shop">Craftly</li>
      <li class="contact-item contact-phone">
        <svg viewBox="0 0 24 24" aria-hidden="true">
          <path d="M7 2.5c1 0 1.6.6 2 1.6l1 3c.2.8 0 1.4-.6 1.9L8.2 10c.8 2 2.4 3.9 4.6 5.3l1.3-1.1c.6-.5 1.3-.6 2-.2l2.8 1.4c.9.5 1.2 1.2.9 2.1l-.6 1.7c-.4 1.1-1.4 1.7-2.6 1.5C10 19.7 4.5 13.4 4.2 6.2 4.1 4.9 4.8 3.6 6 3Z" fill="var(--brand-blue)"/>
        </svg>
        0412873905
      </li>
      <li class="contact-item contact-email">
        <svg viewBox="0 0 24 24" aria-hidden="true" fill="none" stroke="var(--brand-blue)" stroke-width="1.6">
          <rect x="2.5" y="6" width="19" height="12.5" rx="1"/>
          <polyline points="2.5,6.5 12,13.5 21.5,6.5"/>
        </svg>
        info@ tulipsturngold.com.au
      </li>
      <li class="contact-item contact-web">
        <svg viewBox="0 0 24 24" aria-hidden="true" fill="none" stroke="var(--brand-blue)" stroke-width="1.4">
          <circle cx="12" cy="12" r="9.5"/>
          <ellipse cx="12" cy="12" rx="4.5" ry="9.5"/>
          <line x1="12" y1="2.5" x2="12" y2="21.5"/>
          <line x1="2.5" y1="12" x2="21.5" y2="12"/>
          <line x1="4" y1="7.5" x2="20" y2="7.5"/>
          <line x1="4" y1="16.5" x2="20" y2="16.5"/>
        </svg>
        www.tulipsturngold.com.au
      </li>
      <li class="contact-item contact-social">
        <svg viewBox="0 0 24 24" aria-hidden="true" fill="none" stroke="var(--brand-blue)" stroke-width="1.6">
          <rect x="3" y="3" width="18" height="18" rx="2"/>
        </svg>
        Tulips Turn Gold
      </li>
    </ul>

    <svg class="tagline-band" viewBox="0 0 1100 152" preserveAspectRatio="none" aria-hidden="true">
      <path fill="var(--brand-blue)" d="M0 2
        a25 8 0 0 0 50 0 a25 8 0 0 0 50 0 a25 8 0 0 0 50 0 a25 8 0 0 0 50 0
        a25 8 0 0 0 50 0 a25 8 0 0 0 50 0 a25 8 0 0 0 50 0 a25 8 0 0 0 50 0
        a25 8 0 0 0 50 0 a25 8 0 0 0 50 0 a25 8 0 0 0 50 0 a25 8 0 0 0 50 0
        a25 8 0 0 0 50 0 a25 8 0 0 0 50 0 a25 8 0 0 0 50 0 a25 8 0 0 0 50 0
        a25 8 0 0 0 50 0 a25 8 0 0 0 50 0 a25 8 0 0 0 50 0 a25 8 0 0 0 50 0
        a25 8 0 0 0 50 0 a25 8 0 0 0 50 0
        V152 H0 Z"/>
    </svg>
    <p class="tagline">Bringing the old back to new</p>
  </div>
</body>
</html>
```